UNDER ONE [BRIGHT] LANTERN, Shape your path

We are looking for a cover refresh of an existing bestselling book that is going into 3rd edition print this year.
The book is an inspirational as well as educational book that has become recognized as one of the most comprehensive, actionable, personal and financial planning resources available today for families, individuals and business owners alike.
Comprised of three true stories of loss, learning to live and love again and a 30 page checklist at the back of the book it contains tips and strategies for everyone to help them to get their personal and financial lives in order while they can.
The cover must have the following:
1. Appeal to a broad audience/both personal and corporate
2. Include Mira Tollenkamp Bestselling Author
3. Include introduction of a new Afterword
4. 3rd Edition
5. Colors to remain the same – red, black and white
6. The title must remain in caps and the word [BRIGHT] must have the brackets around it
We have also added a current copy of the second edition to help you. For your information our website is www.thetollenkampcircle.example
Reason: We have narrowed it down to our top 3 designs. We are submitting the covers to our community for them to pick the top cover. Good luck to everyone

```html
<!DOCTYPE html>
<html lang="en">
<head>
<meta charset="utf-8">
<title>Under One [Bright] Lantern – Third Edition Cover</title>
<link rel="stylesheet" href="https://fonts.googleapis.com/css2?family=Bebas+Neue&family=Barlow:wght@500;600&family=Italianno&display=swap">
<style>
  :root {
    --page-bg: #ffffff;
    --cover-light: #fbfbfb;
    --cover-mid: #e6e6e6;
    --cover-dark: #cfcfcf;
    --ink: #0c0c0c;
    --accent-red: #b5140f;
    --gold: #b8862a;
    --gold-light: #e2b851;
    --badge: #3f3f3f;
    --author: #2b2b2b;
  }
  * { margin: 0; padding: 0; box-sizing: border-box; }
  html, body {
    width: 1200px; height: 1089px; overflow: hidden;
    background: var(--page-bg);
  }
  .cover {
    position: absolute; left: 237px; top: 0;
    width: 726px; height: 1089px; overflow: hidden;
    background:
      radial-gradient(ellipse at 50% 85%, var(--cover-light) 0%, rgba(251,251,251,0) 60%),
      linear-gradient(180deg, var(--cover-dark) 0%, var(--cover-mid) 35%, #f1f1f1 65%, var(--cover-light) 100%);
  }
  .title {
    position: absolute; left: 0; top: 22px; width: 100%;
    font-family: "Bebas Neue", "Oswald", sans-serif;
    text-align: center; color: var(--ink);
    font-size: 178px; line-height: 176px; letter-spacing: 1px;
  }
  .title .line { display: block; }
  .title .highlight { color: var(--accent-red); }
  .edition-badge {
    position: absolute; left: 0; top: 551px;
    width: 91px; height: 55px; background: var(--badge);
    color: #fff; font-family: "Barlow", sans-serif; font-weight: 600;
    font-size: 13px; line-height: 17px; text-align: center;
    padding-top: 11px; letter-spacing: 0.5px;
  }
  .tagline {
    position: absolute; left: 318px; top: 548px;
    font-family: "Italianno", cursive; font-size: 62px;
    color: var(--gold); white-space: nowrap;
  }
  .nib-art { position: absolute; left: 210px; top: 545px; }
  .author {
    position: absolute; left: 0; width: 100%; top: 948px;
    text-align: center; font-family: "Barlow", sans-serif;
    color: var(--author);
  }
  .author-name {
    font-weight: 600; font-size: 44px; letter-spacing: 6px; line-height: 50px;
  }
  .author-role {
    font-weight: 500; font-size: 31px; letter-spacing: 1.5px; line-height: 40px; margin-top: 6px;
  }
</style>
</head>
<body>
  <main class="cover">
    <h1 class="title">
      <span class="line">UNDER ONE</span>
      <span class="line highlight">[BRIGHT]</span>
      <span class="line">LANTERN</span>
    </h1>

    <div class="edition-badge">THIRD<br>EDITION</div>
    <p class="tagline">Shape your path</p>

    <svg class="nib-art" width="320" height="370" viewBox="0 0 320 370">
      <defs>
        <linearGradient id="nib-gold" x1="0" y1="0" x2="1" y2="1">
          <stop offset="0" stop-color="var(--gold-light)"/>
          <stop offset="0.55" stop-color="var(--gold)"/>
          <stop offset="1" stop-color="#8a5e17"/>
        </linearGradient>
        <linearGradient id="stroke-red" x1="0" y1="0" x2="1" y2="0">
          <stop offset="0" stop-color="var(--accent-red)" stop-opacity="0"/>
          <stop offset="1" stop-color="var(--accent-red)"/>
        </linearGradient>
      </defs>
      <g role="img" aria-label="Golden fountain pen nib angled down to the right, its tip touching the page">
        <rect x="105" y="-10" width="78" height="330" rx="36" fill="url(#nib-gold)" transform="rotate(-35 144 160)"/>
      </g>
      <path class="ink-stroke" d="M8 344 Q 150 334 308 350 Q 160 342 8 346 Z" fill="url(#stroke-red)"/>
    </svg>

    <div class="author">
      <p class="author-name">MIRA TOLLENKAMP</p>
      <p class="author-role">BESTSELLING AUTHOR</p>
    </div>
  </main>
</body>
</html>
```